Stationary/Business Card for Maple Freight Hauling Company
Maple Freight
Professional
Dana R Whitcomb
Managing Partner
Maple Freight LLC
4172 Old Harbor Lane
Jacksonville, Fl 32299
dana@maplefreight-example.com
www.maplefreightlines-example.com
We are looking for stationary and business cards that can easily be printed in either black and white or color. We're open to any and all ideas. Also, just a heads up but the web address listed above is still a dummy site so it will be a bit useless for inspiration. Thank you in advance for all your hard work.

```html
<!DOCTYPE html>
<html lang="en">
<head>
<meta charset="utf-8">
<title>Maple Freight — Stationery Set</title>
<link href="https://fonts.googleapis.com/css2?family=Open+Sans:wght@400;600;800&display=swap" rel="stylesheet">
<style>
  :root{
    --board:#141414;
    --board-light:#2a2a2a;
    --paper:#ffffff;
    --brand-green:#3aa845;
    --brand-dark:#555555;
    --ink:#444444;
    --ink-soft:#888888;
    --rule:#bbbbbb;
  }
  *{margin:0;padding:0;box-sizing:border-box}
  html,body{width:1200px;height:696px;overflow:hidden}
  body{
    position:relative;
    background:linear-gradient(90deg,var(--board) 0%,var(--board-light) 50%,var(--board) 100%);
    font-family:"Open Sans",sans-serif;
    color:var(--ink);
  }
  .sheet{position:absolute;background:var(--paper);overflow:hidden}
  .wordmark{
    font-family:"Open Sans",sans-serif;font-weight:800;color:var(--brand-green);
    white-space:nowrap;display:flex;align-items:center;gap:5px;line-height:1;
  }
  .wordmark .dot{display:inline-block;border-radius:50%;background:var(--brand-green)}
  .details{font-size:5px;line-height:1.55;color:var(--ink-soft);white-space:nowrap}

  /* business card */
  .card-front{left:43px;top:192px;width:257px;height:151px;border-radius:10px}
  .card-front .wordmark{position:absolute;left:14px;top:66px;font-size:14px;gap:4px}
  .card-front .wordmark .dot{width:6px;height:6px}
  .card-front .contact{position:absolute;left:140px;top:22px;border-left:1px solid var(--rule);padding-left:7px}
  .card-front .name{font-size:7px;font-weight:600;color:var(--brand-green);white-space:nowrap}
  .card-front .role{font-size:5.5px;color:var(--ink);margin-bottom:8px;white-space:nowrap}
  .card-front .details{font-size:5px}

  .card-back{left:43px;top:360px;width:257px;height:151px;border-radius:10px}

  /* letterhead */
  .letterhead{left:322px;top:36px;width:307px;height:593px}
  .letterhead .wordmark{position:absolute;left:20px;top:46px;font-size:17px}
  .letterhead .wordmark .dot{width:7px;height:7px}
  .letterhead .contact{position:absolute;left:200px;top:46px;border-left:1px solid var(--rule);padding-left:6px}

  /* envelopes */
  .envelope{left:785px;width:379px;height:192px}
  .envelope .flap{position:absolute;left:0;top:0;width:100%;height:100%}
  .envelope .web{position:absolute;left:0;right:0;top:54px;text-align:center;font-size:6px;color:#eeeeee}
  .env-grey{top:36px}
  .env-green{top:271px}
  .env-front{top:480px;height:187px}
  .env-front .wordmark{position:absolute;left:22px;top:60px;font-size:16px}
  .env-front .wordmark .dot{width:6px;height:6px}
  .env-front .contact{position:absolute;left:266px;top:58px;border-left:1px solid var(--rule);padding-left:6px}
</style>
</head>
<body>

<section class="sheet card-front" aria-label="Business card front">
  <div class="wordmark"><span class="dot"></span>Maple Freight</div>
  <div class="contact">
    <p class="name">Dana R Whitcomb</p>
    <p class="role">Managing Partner</p>
    <div class="details">
      <p>Maple Freight LLC</p>
      <p>4172 Old Harbor Lane</p>
      <p>Jacksonville, Fl 32299</p>
      <p style="margin-top:5px">T (904) 555-0142</p>
      <p>F (904) 555-0143</p>
      <p>dana@maplefreight-example.com</p>
      <p>www.maplefreightlines-example.com</p>
    </div>
  </div>
</section>

<section class="sheet card-back" aria-label="Business card back"></section>

<section class="sheet letterhead" aria-label="Letterhead">
  <div class="wordmark"><span class="dot"></span>Maple Freight</div>
  <div class="contact details">
    <p>Maple Freight LLC</p>
    <p>4172 Old Harbor Lane</p>
    <p>Jacksonville, Fl 32299</p>
    <p>T (904) 555-0142</p>
    <p>F (904) 555-0143</p>
    <p>dana@maplefreight-example.com</p>
    <p>www.maplefreightlines-example.com</p>
  </div>
</section>

<section class="sheet envelope env-grey" aria-label="Envelope back, grey flap">
  <svg class="flap" viewBox="0 0 379 192" preserveAspectRatio="none">
    <path d="M0 0 H379 V58 Q370 92 340 92 H39 Q9 92 0 58 Z" fill="#4a4a4a"/>
  </svg>
  <p class="web">www.maplefreightlines-example.com</p>
</section>

<section class="sheet envelope env-green" aria-label="Envelope back, green flap">
  <svg class="flap" viewBox="0 0 379 192" preserveAspectRatio="none">
    <path d="M0 0 H379 V58 Q370 92 340 92 H39 Q9 92 0 58 Z" fill="#3aa845"/>
  </svg>
  <p class="web">www.maplefreightlines-example.com</p>
</section>

<section class="sheet envelope env-front" aria-label="Envelope front">
  <div class="wordmark"><span class="dot"></span>Maple Freight</div>
  <div class="contact details">
    <p>Maple Freight LLC</p>
    <p>4172 Old Harbor Lane</p>
    <p>Jacksonville, Fl 32299</p>
    <p>T (904) 555-0142</p>
    <p>www.maplefreightlines-example.com</p>
  </div>
</section>

</body>
</html>
```